Psychotherapy and emotion coaching with feloQuin requires web design

I need a web design for emotion coaching (release of emotional blockages) (psychotherapy) with the target group trauma-related disorders and anxiety disorders. The website should be clear and well-organized, i.e. rather simple. The colors should be light, blue, green and yellow are desirable. The design should radiate security.

A logo already exists and should be used appropriately.

Three columns should describe the following
-Emotion regulation
-Imaginative structure constellations
-Ego-State-Therapy

An outdated draft can be seen here:
www.klarer-mutweg.example
The website should advertise coded in Wordpress.

I need the landing page, for which there are drafts now, and at least one more page (maybe a template) for further information (like "About me")

Target Market(s)

Clients for coaching and therapy with trauma or axienty disorders;

Coding

Coded - Design and coding required

Number of Pages Required

3 page

Font styles to use
Sans Serif

Colors
0054AA
0677BA
7BADD7
CADEEF
E8F1F8
59FF00
82FF00
B8FF75
E3FFCB
F4FFEA
FFF300
FFF600
FEFA6F
FFFEC7
FFFEE8

Requirements
Nice to have
• Title: "More happiness and satisfaction in life"
Should not have
• "Therapy" should not be listed in the header; Instead "More happiness and satisfaction in life"

```html
<!DOCTYPE html>
<html lang="de">
<head>
<meta charset="utf-8">
<title>Stille Quelle – Mehr Lebensfreude finden</title>
<link href="https://fonts.googleapis.com/css2?family=Roboto:wght@400;500;700&display=swap" rel="stylesheet">
<style>
:root{
  --blue:#3f7be6; --blue-dark:#2f66d1; --blue-light:#eef4fd;
  --green:#3cb043; --green-light:#f1faec; --green-band:#5fd12a;
  --yellow:#f5c400; --ink:#222; --muted:#666; --white:#fff;
}
*{box-sizing:border-box;margin:0;padding:0}
html,body{width:1200px;height:4491px;overflow:hidden}
body{font-family:'Roboto',sans-serif;color:var(--ink);position:relative;background:var(--white)}
.abs{position:absolute}
.header{top:0;left:0;width:1200px;height:84px;background:#fff;z-index:5}
.brand{left:110px;top:24px;font-size:14px;line-height:18px;color:#444}
.brand .dot{display:inline-block;width:34px;height:34px;border-radius:50%;background:var(--yellow);vertical-align:middle;margin-right:10px;position:relative;top:-8px;float:left}
.brand .sub{color:#e0a100}
.nav{left:444px;top:35px;display:flex;gap:20px;font-size:14px;color:#333}
.nav .active{color:var(--green);font-weight:700;text-decoration:underline}
.lang{left:1003px;top:32px;font-size:14px;color:#333}
.lang .flag{display:inline-block;width:22px;height:22px;border-radius:50%;background:linear-gradient(#222 0 33%,#d00 33% 66%,#fc0 66%);vertical-align:middle;margin-right:6px}
.hero{top:84px;left:0;width:1200px;height:742px}
.hero-photo{position:absolute;inset:0;background:radial-gradient(circle at 30% 30%,#f3d6b0,#c98a4a 45%,#6a7a2a 80%,#8a9a3a)}
.hero-text{left:0;width:1200px;text-align:center;color:#fff;text-shadow:0 2px 6px rgba(0,0,0,.35)}
.btn{display:inline-flex;align-items:center;gap:10px;padding:0 20px;height:46px;font-size:14px;font-weight:700;color:#fff;background:var(--green);text-transform:uppercase}
.btn.blue{background:var(--blue)}
.btn::after{content:"";width:12px;height:12px;border-radius:50%;background:#fff}
.dash{width:50px;height:3px;background:var(--yellow)}
h2{font-size:38px;font-weight:500;color:#222}
.card{width:300px;height:405px;background:#fff;box-shadow:0 4px 16px rgba(0,0,0,.18);border-radius:8px;text-align:center;padding:12px}
.card.hl{border:3px solid var(--green)}
.card .ph{height:206px;border-radius:4px}
.card h3{font-size:15px;font-weight:500;margin:28px 10px 10px;line-height:20px}
.card p{font-size:13px;color:var(--muted);line-height:22px;padding:0 8px}
.card .more{display:block;margin-top:12px;color:var(--green);font-size:13px;font-weight:700}
.list li{list-style:none;position:relative;padding-left:36px;font-size:15px;line-height:27px;color:#333;margin-bottom:12px}
.list li::before{content:"";position:absolute;left:0;top:50%;margin-top:-8px;width:16px;height:16px;border-radius:50%;background:var(--green)}
.text p{font-size:15px;line-height:27px;color:#333;text-align:justify;margin-bottom:14px}
.footer-h{font-size:20px;font-weight:700;color:#fff}
.contact{left:115px;color:#fff;font-size:15px;line-height:25px;padding-left:60px}
.contact b{display:block;font-weight:700}
.contact svg{position:absolute;left:0;top:4px}
.field{background:#fff;height:40px;font-size:12px;color:#777;padding:12px 16px}
</style>
</head>
<body>

<header class="abs header">
  <div class="abs brand"><span class="dot"></span>Stille Quelle<br><span class="sub">…zur Lebensfreude</span></div>
  <nav class="abs nav"><span class="active">START</span><span>JONAS</span><span>UBER EMDR</span><span>FELOQUIN</span><span>ANGEBOT</span><span>KONTAKT</span></nav>
  <div class="abs lang"><span class="flag"></span>GER ⌄</div>
</header>

<section class="abs hero">
  <div class="hero-photo" role="img" aria-label="Frau mit geschlossenen Augen im warmen Sonnenlicht"></div>
  <svg class="abs" style="left:0;top:0" width="1200" height="742" viewBox="0 0 1200 742">
    <polygon points="0,582 600,706 1200,582 1200,742 0,742" fill="var(--blue)"/>
    <polygon points="0,608 600,728 1200,608 1200,742 0,742" fill="#fff"/>
  </svg>
  <div class="abs hero-text" style="top:290px;font-size:34px;font-weight:700">Belastungen loslassen !</div>
  <div class="abs hero-text" style="top:335px;font-size:72px;font-weight:700">Mehr Lebensfreude finden!</div>
  <div class="abs hero-text" style="top:436px;font-size:20px;font-weight:500">Ich reuen mich, Sie bei bei seelischen Nöten oder in Krisen zu unterstützen.</div>
  <div class="abs" style="left:520px;top:488px"><span class="btn" style="height:44px">Mehr lesen</span></div>
</section>

<section>
  <div class="abs dash" style="left:575px;top:874px"></div>
  <h2 class="abs" style="left:0;width:1200px;text-align:center;top:890px">Meine Leistungen</h2>
  <div class="abs card" style="left:112px;top:973px">
    <div class="ph" role="img" aria-label="Zwei Kinder laufen über eine Sommerwiese" style="background:linear-gradient(#b9d6e8,#9dbb5a)"></div>
    <h3>Emotionsregulation mittels bifokaler Aufmerksamkeit</h3>
    <p>Mittels dieser Technik werden gezielt die im Gehirn gespeicherten Erfahrungen, die uns blockieren, positiv verändert.</p>
    <span class="more">MEHR LESEN ●</span>
  </div>
  <div class="abs card hl" style="left:450px;top:973px">
    <div class="ph" role="img" aria-label="Lächelndes älteres Paar" style="background:linear-gradient(135deg,#d8d4cc,#8aa2b8)"></div>
    <h3>Systemische Strukturaufstellungen“ einschließlich Familienaufstellungen</h3>
    <p>Wir alle haben überkommene Prägungen und Muster, die immer wieder Konflikte verursachen oder uns ausbremsen.</p>
    <span class="more">MEHR LESEN ●</span>
  </div>
  <div class="abs card" style="left:787px;top:973px">
    <div class="ph" role="img" aria-label="Farbenfrohe Collage vieler Gesichter als innere Anteile" style="background:linear-gradient(135deg,#e0883a,#b04a8a,#4a6ab0)"></div>
    <h3>Arbeit mit Inneren Persönlichkeitsanteilen</h3>
    <p>(auch bekannt als „Ego-State-Coaching“ oder „Inneres Team“). Wenn Kritik manchmal bei dir ein Gefühl von</p>
    <span class="more">MEHR LESEN ●</span>
  </div>
</section>

<svg class="abs" style="left:0;top:1460px" width="1200" height="890" viewBox="0 0 1200 890">
  <polygon points="0,140 600,4 1200,140 1200,750 600,886 0,750" fill="var(--blue)"/>
  <polygon points="0,164 600,28 1200,164 1200,726 600,862 0,726" fill="var(--blue-light)"/>
</svg>
<section>
  <div class="abs dash" style="left:575px;top:1620px"></div>
  <h2 class="abs" style="left:0;width:1200px;text-align:center;top:1636px">Jonas Falkner (Heilprakter für Psychotherapie)</h2>
  <p class="abs" style="left:190px;width:820px;top:1698px;text-align:center;font-size:15px;line-height:28px;color:#333">Wenn Sie gerade beispielweise an einem der folgenden Punkte im Leben angekommen sind, unterstütze ich Sie gerne darin, Wege aus der Krise zu finden und Änderungen herbeizuführen:</p>
  <ul class="abs list" style="left:143px;top:1790px;width:430px">
    <li>Sie haben oder eine Ihnen nahestehende Person hat eine Diagnose zu einer schwerwiegenden Krankheit, wie Krebs bekommen (Psychoonkologie)</li>
    <li>Sie leiden unter Ängsten, Phobien oder Krankheiten, wie Tinnitus</li>
    <li>Sie haben schlimme bzw. traumatische Erfahrungen gemacht und/oder leiden an deren Folgen bzw. an einer posttraumatischen Belastungsstörung</li>
    <li>Sie haben Schwierigkeiten im Beruf oder mit Ihrem Partner / Ihrer PartnerIn.</li>
  </ul>
  <div class="abs" style="left:145px;top:2114px"><span class="btn">Mehr lesen</span></div>
  <div class="abs" role="img" aria-label="Beratungsgespräch zweier Frauen im Sitzen" style="left:635px;top:1800px;width:420px;height:360px;border:4px solid #fff;box-shadow:0 4px 14px rgba(0,0,0,.2);background:linear-gradient(135deg,#9aa3ad,#5d6b78)"></div>
</section>

<section>
  <div class="abs" style="left:192px;top:2405px;width:363px;height:359px;border:3px solid var(--green)"></div>
  <div class="abs" role="img" aria-label="Leuchtendes Gehirn in einer Hand" style="left:106px;top:2430px;width:410px;height:395px;border-radius:18px;background:radial-gradient(circle at 50% 40%,#c8406a,#1f5a6a 55%,#0e2a36)"></div>
  <div class="abs" role="img" aria-label="Weg durch eine grüne Birkenallee" style="left:331px;top:2672px;width:253px;height:237px;border-radius:10px;border:4px solid #fff;background:linear-gradient(#c9dbe6,#8fb060 60%,#c9b995)"></div>
  <div class="abs dash" style="left:640px;top:2411px"></div>
  <h2 class="abs" style="left:640px;top:2427px">Über EMDR</h2>
  <div class="abs text" style="left:640px;top:2480px;width:452px">
    <p>Unser Gehirn merkt sich Erfahrungen, die schwerwiegend waren oder uns in einer traumatischen Situation überfordert haben. Wenn wir unbewusst an solche Erfahrungen erinnert werden, sind wir nicht mehr voll und ganz handlungsfähig und fühlen uns schlecht</p>
    <p>EMDR steht für Eye Movement Desensitization and Reprocessing, was auf Deutsch Desensibilisierung und Verarbeitung durch Augenbewegung bedeutet. Dr. Lena Marwitz entwickelte diese Psychotherapieform zur Behandlung von Trauma folg estörungen Ende der 80er Jahre des letzten Jahrhunderts</p>
    <p>EMDR hilft dabei, traumatische Erlebnisse zu verarbeiten. Das Gehirn verfügt über Selbstheilungskräfte, die mittels EMDR aktiviert werden können.</p>
  </div>
  <div class="abs" style="left:640px;top:2868px"><span class="btn">Mehr lesen</span></div>
</section>

<svg class="abs" style="left:0;top:3000px" width="1200" height="1491" viewBox="0 0 1200 1491">
  <polygon points="0,148 600,4 1200,148 1200,1491 0,1491" fill="var(--green-band)"/>
  <polygon points="0,170 600,26 1200,170 1200,1491 0,1491" fill="var(--green-light)"/>
  <polygon points="0,654 600,800 1200,654 1200,1491 0,1491" fill="var(--green-band)"/>
  <polygon points="0,654 600,778 1200,654 1200,1491 0,1491" fill="var(--blue)"/>
  <polygon points="0,1411 1200,1411 1200,1491 0,1491" fill="var(--blue-dark)"/>
</svg>
<section>
  <div class="abs dash" style="left:575px;top:3113px"></div>
  <h2 class="abs" style="left:0;width:1200px;text-align:center;top:3125px">Angebot</h2>
  <p class="abs" style="left:0;width:1200px;text-align:center;top:3188px;font-size:19px;color:#333">Meine Angebote zu Psychotherapie und Coaching umfassen ..</p>
  <ul class="abs list" style="left:153px;top:3282px;width:460px">
    <li>ein kostenloses Erstgespräch</li>
    <li>Klientenzentrierte Gesprächstherapie nach Paul Hennings</li>
    <li>die Bearbeitung Ihres Themas mittels einer oder em feloQuin-Sitzung oder einer EMDR-Sitzung</li>
    <li>Beratung zu aktuellen Problemen und Krisen</li>
    <li>systemische Therapie (Famailienaufstellung oder imaginative Systemstrukturaufstellung</li>
  </ul>
  <div class="abs" style="left:153px;top:3579px"><span class="btn blue">Mehr lesen</span></div>
  <div class="abs" role="img" aria-label="Leuchtendes Gehirn in einem Kopfprofil" style="left:644px;top:3256px;width:408px;height:408px;border-radius:50%;border:6px solid #fff;box-shadow:0 4px 16px rgba(0,0,0,.15);background:radial-gradient(circle at 50% 40%,#f08a3a,#2a4fb0 55%,#0a1a50)"></div>
</section>

<footer>
  <div class="abs" style="left:0;width:1200px;top:3862px;text-align:center;color:#fff;font-size:20px;line-height:24px"><span style="display:inline-block;width:44px;height:44px;border-radius:50%;background:var(--yellow);vertical-align:middle;margin-right:30px"></span><span style="display:inline-block;vertical-align:middle;text-align:left">Stille Quelle<br>…zur Lebensfreude</span></div>
  <div class="abs" style="left:112px;top:3945px;width:976px;height:1px;background:rgba(255,255,255,.35)"></div>
  <div class="abs footer-h" style="left:115px;top:4000px">Kontaktdetails</div>
  <div class="abs contact" style="top:4055px"><svg width="28" height="36" viewBox="0 0 28 36"><path d="M14 2C7 2 2 7 2 14c0 9 12 20 12 20s12-11 12-20C26 7 21 2 14 2z" fill="#fff"/><circle cx="14" cy="14" r="5" fill="var(--blue)"/></svg>Birkenhang 12<br>38100 Musterstadt</div>
  <div class="abs contact" style="top:4125px"><svg width="36" height="36" viewBox="0 0 36 36"><path d="M8 4l6 6-3 4c2 4 6 8 10 10l4-3 6 6-4 5C16 31 5 20 3 8z" fill="none" stroke="#fff" stroke-width="2"/></svg><b>TELEFONNUMMER</b>0151 000 12 345</div>
  <div class="abs contact" style="top:4200px"><svg width="36" height="28" viewBox="0 0 36 28"><rect x="1" y="1" width="34" height="26" fill="none" stroke="#fff" stroke-width="2"/><path d="M1 1l17 14L35 1M1 27l12-12M35 27L23 15" fill="none" stroke="#fff" stroke-width="2"/></svg><b>E-MAIL</b>kontakt@stille-quelle.example</div>
  <div class="abs contact" style="top:4271px"><svg width="36" height="28" viewBox="0 0 36 28"><rect x="1" y="1" width="34" height="26" fill="none" stroke="#fff" stroke-width="2"/><path d="M1 1l17 14L35 1M1 27l12-12M35 27L23 15" fill="none" stroke="#fff" stroke-width="2"/></svg><b>WEBSEITE</b>www.klarer-mutweg.example</div>
  <div class="abs footer-h" style="left:563px;top:4000px">In Kontakt kommen</div>
  <div class="abs field" style="left:563px;top:4064px;width:257px">👤 Name</div>
  <div class="abs field" style="left:833px;top:4064px;width:257px">📞 Phone Number</div>
  <div class="abs field" style="left:563px;top:4121px;width:257px">✉ Email Address</div>
  <div class="abs field" style="left:833px;top:4121px;width:257px;background:#eef0f3">✎ Subject</div>
  <div class="abs field" style="left:563px;top:4177px;width:527px;height:86px">💬 Messagge</div>
  <div class="abs" style="left:563px;top:4282px;width:527px;height:44px;background:linear-gradient(90deg,#f5c400,#f9d020);color:#222;font-size:14px;font-weight:700;text-align:center;line-height:44px">SUBMIT NOW</div>
  <div class="abs" style="left:0;width:1200px;top:4447px;text-align:center;color:#fff;font-size:14px">© 2024 Stille Quelle zur Lebensfreude | Alle Rechte vorbehalten</div>
</footer>

</body>
</html>
```